Heat & air company needs eye catching van wrap for our fleet!

Need a van wrap designed for our fleet of vans. It should incorporate our logo, website address, phone number, license number (as it is on existing vans). Should use the blue and red from our logo as the primary colors. Should also mention plumbing under the logo in lighter blue. I really love the ice cubes on the bottom like the example I am attaching. I am attaching examples of existing and others I like from online. I do not want copies. I want unique and using imagination.

Requirements
Must have
• Logo very big. Use blue and red. Have license number same as existing van. Have plumbing under heating & Air Conditioning.

```html
<!DOCTYPE html>
<html lang="en">
<head>
<meta charset="utf-8">
<title>Calder Heating &amp; Air Conditioning – Fleet Wrap</title>
<link rel="stylesheet" href="https://fonts.googleapis.com/css2?family=Questrial&family=Open+Sans:wght@700;800&display=swap">
<style>
  :root {
    --brand-blue: #2c4f9e;
    --brand-navy: #16265a;
    --brand-red: #b8343b;
    --plumbing-blue: #a9cdf5;
    --ice-light: #dcecf8;
    --ice-mid: #8fbbe0;
    --panel-white: #ffffff;
    --page-bg: #f4f5f7;
    --panel-edge: #d6d9de;
  }
  html, body {
    margin: 0;
    padding: 0;
    width: 1200px;
    height: 759px;
    overflow: hidden;
    background: var(--page-bg);
  }
  .wrap-sheet { display: block; width: 1200px; height: 759px; }
  .brand-name { font-family: "Questrial", sans-serif; fill: var(--panel-white); letter-spacing: 1px; }
  .service-line { font-family: "Questrial", sans-serif; fill: var(--panel-white); }
  .service-line .accent { fill: var(--brand-red); }
  .plumbing { font-family: "Questrial", sans-serif; fill: var(--plumbing-blue); }
  .contact { font-family: "Open Sans", sans-serif; font-weight: 800; fill: var(--brand-red); }
  .contact-dark { font-family: "Open Sans", sans-serif; font-weight: 700; fill: #2a2a2a; }
  .service-list { font-family: "Open Sans", sans-serif; font-weight: 700; fill: var(--panel-white); }
  .brand-mark { fill: var(--panel-white); }
  .brand-mark-blue { fill: var(--brand-blue); }
  .divider { stroke: var(--panel-white); stroke-width: 1.5; }
</style>
</head>
<body>
<svg class="wrap-sheet" viewBox="0 0 1200 759" xmlns="http://www.w3.org/2000/svg">
  <defs>
    <linearGradient id="blueBody" x1="0" y1="0" x2="0" y2="1">
      <stop offset="0" stop-color="#3a5fb0"/>
      <stop offset="1" stop-color="#1f3a80"/>
    </linearGradient>
    <linearGradient id="iceBand" x1="0" y1="0" x2="0" y2="1">
      <stop offset="0" stop-color="#2a4a95" stop-opacity="0"/>
      <stop offset="0.35" stop-color="#8fbbe0"/>
      <stop offset="1" stop-color="#dcecf8"/>
    </linearGradient>
    <clipPath id="clipRightSide"><rect x="440" y="80" width="690" height="250" rx="18"/></clipPath>
    <clipPath id="clipLeftSide"><rect x="75" y="435" width="685" height="255" rx="18"/></clipPath>
    <clipPath id="clipRightBlue"><path d="M725,80 C690,140 700,260 800,330 L1130,330 L1130,80 Z"/></clipPath>
    <clipPath id="clipLeftBlue"><path d="M470,435 C505,500 495,620 405,690 L75,690 L75,435 Z"/></clipPath>
  </defs>

  <!-- Front hood panel -->
  <g class="panel panel-front">
    <rect x="85" y="130" width="290" height="100" rx="14" fill="var(--panel-white)" stroke="var(--panel-edge)"/>
    <rect class="brand-mark-blue" x="122" y="162" width="38" height="38" rx="6"/>
    <text class="contact-dark" x="182" y="178" font-size="21">555-014-2287</text>
    <text class="contact-dark" x="182" y="202" font-size="17">calderair.com</text>
  </g>

  <!-- Passenger side panel -->
  <g class="panel panel-side-right" clip-path="url(#clipRightSide)">
    <rect x="440" y="80" width="690" height="250" fill="var(--brand-red)"/>
    <path d="M600,80 C555,140 555,230 615,330 L1130,330 L1130,80 Z" fill="var(--panel-white)"/>
    <path d="M710,80 C675,140 685,260 785,330 L1130,330 L1130,80 Z" fill="var(--brand-navy)"/>
    <path d="M725,80 C690,140 700,260 800,330 L1130,330 L1130,80 Z" fill="url(#blueBody)"/>
    <rect x="690" y="262" width="440" height="68" fill="url(#iceBand)" clip-path="url(#clipRightBlue)" role="img" aria-label="Band of ice cubes along the lower edge"/>
    <rect class="brand-mark" x="742" y="104" width="44" height="44" rx="7"/>
    <text class="brand-name" x="800" y="144" font-size="50">CALDER</text>
    <text class="service-line" x="802" y="164" font-size="17"><tspan class="accent">Heating</tspan> &amp; Air Conditioning</text>
    <line class="divider" x1="812" y1="179" x2="872" y2="179"/>
    <text class="plumbing" x="890" y="185" font-size="20">Plumbing</text>
    <line class="divider" x1="990" y1="179" x2="1065" y2="179"/>
    <text class="contact" x="584" y="192" font-size="18">555-014-2287</text>
    <text class="contact" x="652" y="262" font-size="14">calderair.com</text>
  </g>

  <!-- Driver side panel -->
  <g class="panel panel-side-left" clip-path="url(#clipLeftSide)">
    <rect x="75" y="435" width="685" height="255" fill="var(--panel-white)"/>
    <path d="M640,435 C610,520 640,620 610,690 L760,690 L760,435 Z" fill="var(--brand-red)"/>
    <path d="M485,435 C520,500 510,620 420,690 L75,690 L75,435 Z" fill="var(--brand-navy)"/>
    <path d="M470,435 C505,500 495,620 405,690 L75,690 L75,435 Z" fill="url(#blueBody)"/>
    <rect x="75" y="620" width="440" height="70" fill="url(#iceBand)" clip-path="url(#clipLeftBlue)" role="img" aria-label="Band of ice cubes along the lower edge"/>
    <rect class="brand-mark" x="130" y="464" width="44" height="44" rx="7"/>
    <text class="brand-name" x="188" y="504" font-size="50">CALDER</text>
    <text class="service-line" x="190" y="524" font-size="17"><tspan class="accent">Heating</tspan> &amp; Air Conditioning</text>
    <line class="divider" x1="200" y1="542" x2="262" y2="542"/>
    <text class="plumbing" x="282" y="548" font-size="20">Plumbing</text>
    <line class="divider" x1="385" y1="542" x2="455" y2="542"/>
    <text class="contact" x="505" y="554" font-size="18">555-014-2287</text>
    <text class="contact" x="434" y="624" font-size="14">calderair.com</text>
  </g>

  <!-- Rear doors panel -->
  <g class="panel panel-rear">
    <rect x="835" y="400" width="310" height="210" rx="16" fill="url(#blueBody)"/>
    <line x1="990" y1="400" x2="990" y2="488" stroke="var(--brand-navy)" stroke-width="2"/>
    <rect class="brand-mark" x="893" y="500" width="28" height="28" rx="5"/>
    <text class="brand-name" x="930" y="525" font-size="30">CALDER</text>
    <text class="service-line" x="932" y="538" font-size="10">Heating &amp; Air Conditioning</text>
    <text class="service-list" x="892" y="555" font-size="11">• Residential</text>
    <text class="service-list" x="892" y="569" font-size="11">• Commercial</text>
    <text class="service-list" x="988" y="555" font-size="11">• Sales | Service</text>
    <text class="service-list" x="988" y="569" font-size="11">• Installation</text>
    <text class="contact" x="866" y="588" font-size="15">555-014-2287 | calderair.com</text>
  </g>
</svg>
</body>
</html>
```